Maple Ridge business card design

Card needs to include the following text/items:
Company Logo
Rupert Hollis
Phone # - 517-386-9042
service@mapleridgelandscaping.example
Lawn & landscape maintenance services

```html
<!DOCTYPE html>
<html lang="en">
<head>
<meta charset="utf-8">
<title>Maple Ridge Landscaping – Business Card</title>
<link rel="stylesheet" href="https://fonts.googleapis.com/css2?family=Inter:wght@500;600;700&display=swap">
<style>
  :root {
    --backdrop: #cbcbcb;
    --card-white: #ffffff;
    --brand-green: #1f8f40;
    --brand-green-light: #36b04a;
    --brand-green-dark: #1a7a36;
    --logo-green: #145a2a;
    --accent-yellow: #f2e21b;
    --text-light: #ffffff;
  }
  * { margin: 0; padding: 0; box-sizing: border-box; }
  html, body {
    width: 672px;
    height: 1200px;
    overflow: hidden;
    background: var(--backdrop);
    font-family: "Inter", Arial, sans-serif;
  }
  .canvas {
    position: relative;
    width: 672px;
    height: 1200px;
  }
  .card {
    position: absolute;
    left: 56px;
    width: 560px;
    height: 320px;
    box-shadow: 0 14px 22px rgba(0,0,0,0.22);
    overflow: hidden;
  }
  .card-front {
    top: 240px;
    background: var(--card-white);
    display: flex;
    align-items: center;
    justify-content: center;
  }
  .front-brand {
    display: flex;
    align-items: center;
    gap: 14px;
  }
  .brand-dot {
    width: 30px;
    height: 30px;
    border-radius: 50%;
    background: var(--logo-green);
  }
  .brand-name {
    font-weight: 700;
    font-size: 38px;
    letter-spacing: -0.5px;
    color: var(--logo-green);
  }
  .card-back {
    top: 620px;
    background: radial-gradient(circle at 50% 50%, var(--brand-green-light) 0%, var(--brand-green) 55%, var(--brand-green-dark) 100%);
    color: var(--text-light);
  }
  .back-emblem {
    position: absolute;
    left: 305px;
    top: 20px;
    width: 255px;
    height: 255px;
    border-radius: 50%;
    background: rgba(20, 110, 50, 0.35);
  }
  .back-brand {
    position: absolute;
    left: 69px;
    top: 82px;
    font-weight: 700;
    font-size: 27px;
    letter-spacing: -0.3px;
  }
  .holder-name {
    position: absolute;
    left: 69px;
    top: 180px;
    font-weight: 700;
    font-size: 20px;
    letter-spacing: -0.6px;
  }
  .holder-name .surname { color: var(--accent-yellow); }
  .service-line {
    position: absolute;
    left: 69px;
    top: 213px;
    font-weight: 600;
    font-size: 14px;
    line-height: 16px;
    letter-spacing: -0.5px;
  }
  .contact-list {
    position: absolute;
    left: 272px;
    top: 214px;
    list-style: none;
    font-weight: 500;
    font-size: 13px;
    letter-spacing: -0.4px;
  }
  .contact-list li {
    display: flex;
    align-items: center;
    gap: 9px;
    height: 17px;
  }
  .contact-icon { width: 12px; height: 12px; flex: none; }
</style>
</head>
<body>
<main class="canvas">
  <section class="card card-front" aria-label="Card front">
    <div class="front-brand">
      <span class="brand-dot"></span>
      <span class="brand-name">Maple Ridge</span>
    </div>
  </section>

  <section class="card card-back" aria-label="Card back">
    <div class="back-emblem" role="img" aria-label="Faint brand emblem decoration"></div>
    <div class="back-brand">Maple Ridge</div>
    <div class="holder-name">Rupert <span class="surname">Hollis</span></div>
    <div class="service-line">Lawn &amp; Landscape<br>Maintenance Services</div>
    <ul class="contact-list">
      <li>
        <svg class="contact-icon" viewBox="0 0 24 24" fill="none" stroke="#f2e21b" stroke-width="2" stroke-linejoin="round"><path d="M5 3h4l2 5-3 2a11 11 0 0 0 6 6l2-3 5 2v4a2 2 0 0 1-2 2A18 18 0 0 1 3 5a2 2 0 0 1 2-2z"/></svg>
        <span>517-386-9042</span>
      </li>
      <li>
        <svg class="contact-icon" viewBox="0 0 24 24" fill="none" stroke="#f2e21b" stroke-width="2" stroke-linejoin="round"><rect x="3" y="5" width="18" height="14" rx="1"/><path d="M3 6l9 7 9-7"/></svg>
        <span>service@mapleridgelandscaping.example</span>
      </li>
    </ul>
  </section>
</main>
</body>
</html>
```